Marcus Delwyn-Hart Finance

Need a personal website advertising Equipment Finance,Business Finance,Commercial Finance, Construction Finance, Bridging Finance. Similar websites are www.qorvimark.com.au / www.talsbrio.com.au / www.zpk7.com.au /wwwlemberwick.com.au

Target Market(s)

Business People

Industry/Entity Type

Business

Number of Pages Required

3 page

Font styles to use
Serif
Sans Serif

Requirements
Must have
• All i want is a simple corporate looking website advertising Equipment Finance, Commercial Finance, Construction Finance, Business Finance, Bridging Finance,

```html
<!DOCTYPE html>
<html lang="en">
<head>
<meta charset="utf-8">
<title>Marcus Delwyn-Hart Finance</title>
<link href="https://fonts.googleapis.com/css2?family=Open+Sans:wght@400;600;700&family=Roboto:wght@300;400;500&family=Tinos&display=swap" rel="stylesheet">
<style>
:root{
  --blue:#29a8e0;
  --blue-dark:#1f9bd3;
  --ink:#333;
  --muted:#666;
  --light:#f0f0f0;
  --white:#fff;
}
*{margin:0;padding:0;box-sizing:border-box}
html,body{width:736px;height:1200px;overflow:hidden}
body{position:relative;background:var(--white);font-family:'Open Sans',sans-serif;color:var(--ink)}
.abs{position:absolute}

/* header */
.logo-mark{left:61px;top:12px;width:40px;height:40px;border-radius:50%;background:var(--blue)}
.logo-name{left:110px;top:18px;font-family:'Tinos',serif;font-size:21px;color:#555;letter-spacing:-.3px;white-space:nowrap}
.contact-item{top:21px;display:flex;align-items:center;gap:7px;font-size:8px;color:#999;white-space:nowrap}
.contact-item b{font-weight:400;color:var(--blue)}
.contact-icon{width:22px;height:22px;border-radius:50%;background:var(--blue);display:flex;align-items:center;justify-content:center}

/* nav */
.nav{left:0;top:62px;width:736px;height:26px;background:var(--blue)}
.nav ul{list-style:none;position:absolute;left:61px;top:0;height:26px;display:flex;border-left:1px solid rgba(255,255,255,.25)}
.nav li{height:26px;display:flex;align-items:center;justify-content:center;font-size:6.6px;color:var(--white);text-transform:uppercase;white-space:nowrap;border-right:1px solid rgba(255,255,255,.25)}

/* hero */
.hero{left:0;top:88px;width:736px;height:268px;background:linear-gradient(180deg,#c9d6e0 0%,#dfe6ea 45%,#c8d3b4 75%,#a9bd83 100%)}
.hero-photo{left:390px;top:88px;width:346px;height:268px;background:radial-gradient(ellipse at 55% 55%,#d9b59a 0%,#c9a080 30%,rgba(120,140,90,.25) 60%,rgba(0,0,0,0) 75%)}
.hero-title{left:61px;top:152px;font-family:'Roboto',sans-serif;font-weight:300;font-size:24px;color:#444;white-space:nowrap}
.hero-text{left:61px;top:190px;width:280px;font-family:'Roboto',sans-serif;font-weight:300;font-size:12.6px;line-height:19px;color:#444}
.btn{background:var(--blue);color:var(--white);font-weight:700;text-transform:uppercase;display:flex;align-items:center;justify-content:center;border-radius:2px;white-space:nowrap}
.hero-btn{left:61px;top:261px;width:101px;height:26px;font-size:8.5px}
.dots{left:353px;top:340px;display:flex;gap:3px}
.dots span{width:5px;height:5px;border-radius:50%;background:rgba(255,255,255,.7)}
.dots span:first-child{background:var(--blue)}

/* welcome */
.section-title{font-size:12px;font-weight:700;text-transform:uppercase;color:var(--ink);white-space:nowrap}
.welcome-title{left:0;width:736px;top:390px;text-align:center}
.welcome-text{left:116px;width:504px;top:416px;text-align:center;font-size:6.3px;line-height:14.8px;color:var(--muted)}

/* service cards */
.card{top:489px;width:194px;height:131px;background:#555;box-shadow:0 6px 6px -3px rgba(0,0,0,.35)}
.card-label{position:absolute;left:0;top:87px;min-width:129px;height:36px;background:var(--blue);padding:6px 12px 0;color:var(--white);white-space:nowrap}
.card-label h3{font-size:9.4px;line-height:12px;font-weight:700;text-transform:uppercase}
.card-label p{font-size:6.3px;line-height:9px;margin-top:1px}
.slider-arrow{top:545px}

/* profile */
.profile-frame{left:61px;top:671px;width:162px;height:163px;border:1px solid #ddd;background:#f4f4f4;padding:4px}
.profile-photo{width:100%;height:100%;background:linear-gradient(180deg,#d4d4d4 0%,#bdbdbd 55%,#3a3a40 75%,#2b2b30 100%)}
.profile-name{left:258px;top:677px}
.profile-text{left:258px;top:700px;width:418px;font-size:6.3px;line-height:14.6px;color:var(--muted)}
.profile-btn{left:258px;top:800px;width:87px;height:25px;font-size:7px}

/* news */
.news{left:0;top:871px;width:736px;height:143px;background:var(--light)}
.news-title{left:61px;top:891px;font-family:'Roboto',sans-serif;font-weight:500;font-size:12px;color:var(--ink)}
.news-item{top:926px;width:200px;height:56px}
.news-thumb{position:absolute;left:0;top:0;width:63px;height:56px;border:2px solid var(--white);box-shadow:0 0 0 1px #ddd}
.news-body{position:absolute;left:76px;top:0}
.news-body h4{font-size:7.6px;font-weight:700;color:var(--blue)}
.news-body p{font-size:6.3px;line-height:11.6px;color:var(--muted);margin-top:2px;width:140px}
.news-btn{margin-top:4px;width:48px;height:15px;font-size:5.4px;font-weight:400}

/* footer */
.footer{left:0;top:1014px;width:736px;height:154px;background:var(--blue)}
.footer-col{top:1035px;color:var(--white)}
.footer-col h5{font-size:8.4px;font-weight:700;text-transform:uppercase;margin-bottom:6px;white-space:nowrap}
.footer-col li{list-style:none;font-size:6.4px;line-height:13.6px;white-space:nowrap}
.footer-line{display:flex;align-items:center;gap:6px}
.social{left:539px;top:1121px;display:flex;gap:6px}
.social span{width:16px;height:16px;border-radius:50%;background:var(--white)}
.bottom-bar{left:0;top:1168px;width:736px;height:32px;background:var(--blue-dark);display:flex;align-items:center;justify-content:center;font-size:6.4px;color:var(--white)}
</style>
</head>
<body>

<header>
  <div class="abs logo-mark"></div>
  <div class="abs logo-name">Marcus Delwyn-Hart Finance</div>
  <div class="abs contact-item" style="left:432px">
    <span class="contact-icon"><svg width="10" height="10" viewBox="0 0 24 24"><path fill="#fff" d="M6.6 10.8a15 15 0 0 0 6.6 6.6l2.2-2.2c.3-.3.7-.4 1-.2 1.1.4 2.3.6 3.6.6.6 0 1 .4 1 1V20c0 .6-.4 1-1 1A17 17 0 0 1 3 4c0-.6.4-1 1-1h3.5c.6 0 1 .4 1 1 0 1.3.2 2.5.6 3.6.1.3 0 .7-.2 1z"/></svg></span>
    <span>Phone: <b>61 7 5550 1482</b></span>
  </div>
  <div class="abs contact-item" style="left:575px">
    <span class="contact-icon"><svg width="10" height="10" viewBox="0 0 24 24"><path fill="#fff" d="M6 3h12v5H6zM4 9h16a2 2 0 0 1 2 2v6h-4v4H6v-4H2v-6a2 2 0 0 1 2-2zm4 6v4h8v-4z"/></svg></span>
    <span>Fax: <b>61 7 5550 1483</b></span>
  </div>
</header>

<nav class="abs nav">
  <ul>
    <li style="width:72px">Home</li>
    <li style="width:81px">The Business</li>
    <li style="width:84px">Key People</li>
    <li style="width:80px">Solutions</li>
    <li style="width:79px">Investors</li>
    <li style="width:59px">Blog</li>
    <li style="width:74px">Testimonials</li>
    <li style="width:79px">Contact Us</li>
  </ul>
</nav>

<section>
  <div class="abs hero" role="img" aria-label="Soft blurred meadow and sky background"></div>
  <div class="abs hero-photo" role="img" aria-label="Cupped hands holding a small bonsai tree"></div>
  <h1 class="abs hero-title">Marcus Delwyn-Hart Finance</h1>
  <p class="abs hero-text">We provide Equipment Finance,Business Finance, Commercial Finance, Construction Finance, Bridging Finance.</p>
  <div class="abs btn hero-btn">Contact Here!</div>
  <div class="abs dots"><span></span><span></span><span></span><span></span></div>
</section>

<section>
  <h2 class="abs section-title welcome-title">Welcome to Marcus Delwyn-Hart</h2>
  <p class="abs welcome-text">Lorem Ipsum is simply dummy text of the printing and typesetting industry. Lorem Ipsum has been the industry's standard dummy text ever since the 1500s, when an unknown printer took a galley of type and scrambled it to make a type specimen book. It has survived not only five centuries, but also the leap into electronic typesetting, remaining essentially unchanged...</p>

  <svg class="abs slider-arrow" style="left:37px" width="10" height="18" viewBox="0 0 10 18"><path d="M9 1 1 9l8 8" fill="none" stroke="#bbb" stroke-width="1.2"/></svg>
  <svg class="abs slider-arrow" style="left:694px" width="10" height="18" viewBox="0 0 10 18"><path d="m1 1 8 8-8 8" fill="none" stroke="#bbb" stroke-width="1.2"/></svg>

  <div class="abs card" style="left:61px;background:radial-gradient(circle at 55% 45%,#d8a24a 0%,#6b4a22 30%,#1a1a1a 70%)" role="img" aria-label="Businessman with glowing gears">
    <div class="card-label"><h3>Equipment Finance</h3><p>Click here for view info ➔</p></div>
  </div>
  <div class="abs card" style="left:271px;background:linear-gradient(135deg,#e8e4df 0%,#cfc5b8 50%,#b89a72 100%)" role="img" aria-label="Desk with laptop and financial charts">
    <div class="card-label"><h3>Business Finance</h3><p>Click here for view info ➔</p></div>
  </div>
  <div class="abs card" style="left:482px;background:linear-gradient(180deg,#6d7a8a 0%,#e3a85c 45%,#8a6a4a 70%,#4a4a4a 100%)" role="img" aria-label="City skyline at sunset by the water">
    <div class="card-label"><h3>Commercial Finance</h3><p>Click here for view info ➔</p></div>
  </div>
</section>

<section>
  <div class="abs profile-frame"><div class="profile-photo" role="img" aria-label="Portrait photo of the director in a suit"></div></div>
  <h2 class="abs section-title profile-name">Mr. Marcus Delwyn-Hart</h2>
  <p class="abs profile-text">serves as Operations Director of Orrinvale Financial Services Pty Ltd. Mr. Delwyn-Hart has 16 years experience in the Financial Services and bridging Finance industry, both in Australia, as well as in South Africa. He was employed by the South African based business (KESTRELMOOR FINANCE) for the majority of its operation. He held senior operational positions within Kestrelmoor Finance and provided staff support and direction, training and operational control for the Company. Since the establishment of Orrinvale Financial Services, Mr. Delwyn-Hart has implemented constant Procedures, Policy and system updates to products in order to meet market demands and to minimize risk on Bridging loans originated.</p>
  <div class="abs btn profile-btn">Read More Info</div>
</section>

<section>
  <div class="abs news"></div>
  <h2 class="abs news-title">LATEST NEWS</h2>
  <svg class="abs" style="left:38px;top:949px" width="6" height="10" viewBox="0 0 6 10"><path d="M5 1 1 5l4 4" fill="none" stroke="#bbb"/></svg>
  <svg class="abs" style="left:699px;top:949px" width="6" height="10" viewBox="0 0 6 10"><path d="m1 1 4 4-4 4" fill="none" stroke="#bbb"/></svg>

  <div class="abs news-item" style="left:62px">
    <div class="news-thumb" style="background:linear-gradient(135deg,#f3e6d2,#c9a27a)" role="img" aria-label="Man working on a laptop"></div>
    <div class="news-body"><h4>LOREM IPSUM</h4><p>Lorem Ipsum is simply dummy text of the printing and typesetting...</p><div class="btn news-btn">Click Here</div></div>
  </div>
  <div class="abs news-item" style="left:279px">
    <div class="news-thumb" style="background:linear-gradient(135deg,#c8ccd2,#5a5f6a)" role="img" aria-label="Two colleagues in a meeting"></div>
    <div class="news-body"><h4>LOREM IPSUM</h4><p>Lorem Ipsum is simply dummy text of the printing and typesetting...</p><div class="btn news-btn">Click Here</div></div>
  </div>
  <div class="abs news-item" style="left:489px">
    <div class="news-thumb" style="background:linear-gradient(135deg,#dfe3e6,#b84a45)" role="img" aria-label="People seated in red chairs seen from above"></div>
    <div class="news-body"><h4>LOREM IPSUM</h4><p>Lorem Ipsum is simply dummy text of the printing and typesetting...</p><div class="btn news-btn">Click Here</div></div>
  </div>
</section>

<footer>
  <div class="abs footer"></div>
  <div class="abs footer-col" style="left:77px"><h5>Welcome</h5><ul><li>Home</li><li>The Business</li><li>Key People</li><li>Solutions</li><li>Investors</li><li>News</li><li>Contact Us</li></ul></div>
  <div class="abs footer-col" style="left:202px"><h5>Training and Consulting</h5><ul><li>Equipment Finance</li><li>Business Finance</li><li>Commercial Finance</li><li>Construction Finance</li><li>Bridging Finance</li></ul></div>
  <div class="abs footer-col" style="left:394px"><h5>Information</h5><ul><li>Terms &amp; Conditions</li><li>Privacy Policy</li><li>Disclaimer</li><li>Sitemap</li></ul></div>
  <div class="abs footer-col" style="left:538px"><h5>Contact Info</h5><ul>
    <li>3a 18 Harbour Parade</li><li>Coral Bay, Queensland 4299</li>
    <li class="footer-line" style="margin-top:2px"><svg width="7" height="7" viewBox="0 0 24 24"><path fill="#fff" d="M6.6 10.8a15 15 0 0 0 6.6 6.6l2.2-2.2c.3-.3.7-.4 1-.2 1.1.4 2.3.6 3.6.6.6 0 1 .4 1 1V20c0 .6-.4 1-1 1A17 17 0 0 1 3 4c0-.6.4-1 1-1h3.5c.6 0 1 .4 1 1 0 1.3.2 2.5.6 3.6.1.3 0 .7-.2 1z"/></svg>Phone: 61 7 5550 1482</li>
    <li class="footer-line" style="margin-top:2px"><svg width="7" height="7" viewBox="0 0 24 24"><rect x="3" y="5" width="18" height="14" fill="none" stroke="#fff" stroke-width="2"/><path d="m3 6 9 7 9-7" fill="none" stroke="#fff" stroke-width="2"/></svg>Fax: 61 7 5550 1483</li>
  </ul></div>
  <div class="abs social"><span></span><span></span><span></span><span></span><span></span></div>
  <div class="abs bottom-bar">Copyright © 2017, Marcus Delwyn-Hart. All rights reserved.</div>
</footer>

</body>
</html>
```